Re-design of Business Card

We require a design for our business card.

Korrim is a supplier of industrial packaging specializing in plastic products. We are undergoing a rebranding to appear more corporate. We have changed our company name to korrim and have a new logo.

I have uploaded our old card design with the previous company name.
Don't copy the current design. We are looking for a new design.

Industry/Entity Type

Manufacturing

Contact Information for Business Card

please don't copy the current design. we are looking for a new design.

Font styles to use
Sans Serif

Colors

Designer to choose colors to be used in the design.

Requirements
Must have
• clean and easy to read.

```html
<!DOCTYPE html>
<html lang="en">
<head>
<meta charset="UTF-8">
<title>Korrim Business Card</title>
<link href="https://fonts.googleapis.com/css2?family=Open+Sans:wght@400;700&display=swap" rel="stylesheet">
<style>
  :root {
    --backdrop: #d9d9d6;
    --card: #333335;
    --accent: #f07d1e;
    --ink: #f2f2f2;
    --emboss: #3b3b3e;
  }
  html, body {
    margin: 0;
    width: 1200px;
    height: 801px;
    overflow: hidden;
    background: var(--backdrop);
    font-family: "Open Sans", sans-serif;
  }
  .sheet {
    display: flex;
    gap: 40px;
    justify-content: center;
    align-items: center;
    width: 1200px;
    height: 801px;
  }
  .card {
    position: relative;
    width: 540px;
    height: 309px;
    background: var(--card);
    box-shadow: 0 0 0 2px var(--accent), 0 8px 24px rgba(0,0,0,0.25);
    box-sizing: border-box;
  }
  /* front */
  .brand {
    position: absolute;
    left: 40px;
    top: 0;
    width: 210px;
    height: 100%;
    display: flex;
    align-items: center;
    justify-content: center;
    gap: 10px;
  }
  .brand-mark {
    width: 18px;
    height: 18px;
    background: var(--accent);
  }
  .brand-name {
    color: var(--accent);
    font-weight: 700;
    font-size: 46px;
    letter-spacing: 1px;
    line-height: 1;
  }
  .divider {
    position: absolute;
    left: 270px;
    top: 40px;
    bottom: 40px;
    width: 1px;
    background: var(--accent);
  }
  .details {
    position: absolute;
    left: 292px;
    top: 40px;
    color: var(--ink);
    font-size: 13px;
    line-height: 1.35;
  }
  .person-name {
    color: var(--accent);
    font-weight: 700;
    font-size: 19px;
    margin: 0;
    letter-spacing: 0.5px;
  }
  .person-role { margin: 0 0 12px; font-size: 14px; }
  .address { margin: 0 0 14px; }
  .contact-list { list-style: none; margin: 0; padding: 0; }
  .contact-list li { display: flex; align-items: center; gap: 7px; }
  .contact-list svg { width: 12px; height: 12px; fill: var(--accent); flex: none; }
  /* back */
  .back {
    display: flex;
    align-items: center;
    justify-content: center;
  }
  .back-name {
    color: var(--emboss);
    font-weight: 700;
    font-size: 72px;
    letter-spacing: 2px;
  }
</style>
</head>
<body>
<main class="sheet">
  <section class="card front">
    <div class="brand">
      <span class="brand-mark"></span>
      <span class="brand-name">KORRIM</span>
    </div>
    <div class="divider"></div>
    <div class="details">
      <h1 class="person-name">DARREN HOLT</h1>
      <p class="person-role">Machinery Sales Manager</p>
      <p class="address">48 Ridgeway Rd, Marlow Heights<br>Qld, 4215 Australia</p>
      <ul class="contact-list">
        <li><svg viewBox="0 0 12 12"><path d="M2.5 1l2 2.2-1 1.3c.7 1.5 1.8 2.6 3.3 3.3l1.3-1 2.2 2-1.2 1.7C5.5 10.3 1.7 6.5 1 1.7z"/></svg>1300 458 210</li>
        <li><svg viewBox="0 0 12 12"><path d="M3 0h6v12H3zM4 1.5v8h4v-8z"/></svg>+61 7 3390 1742</li>
        <li><svg viewBox="0 0 12 12"><path d="M3 0h6v3H3zM1 4h10v5H9v3H3V9H1zM4 8v3h4V8z"/></svg>1300 458 210</li>
        <li><svg viewBox="0 0 12 12"><path d="M0 2h12v1L6 7 0 3zM0 4.5l6 4 6-4V10H0z"/></svg>darren@korrim.com.au</li>
        <li><svg viewBox="0 0 12 12"><circle cx="6" cy="6" r="5.5"/></svg>www.korrim.com.au</li>
      </ul>
    </div>
  </section>
  <section class="card back">
    <span class="back-name">KORRIM</span>
  </section>
</main>
</body>
</html>
```